New Television Homescreen Template

We need a new default homescreen design for our televisions. This should reflect our company branding. My company is called Wellward Systems, WSY for short. Our website is www.wsyq.com. We develop televisions and infotainment solutions for the healthcare industry. I am somewhat open to different color palettes but our company colors are blue, black, and white. Our design is constrained by the 9 buttons, however the design of the buttons can be changed. Also, there is a video box on the right side of the screen as shown, this design can also be changed.

Target Market(s)

Hospital Patients

Requirements
Must have
• PSD template.

```html
<!DOCTYPE html>
<html lang="en">
<head>
<meta charset="utf-8">
<title>Wellward Systems – Television Homescreen</title>
<link rel="stylesheet" href="https://fonts.googleapis.com/css2?family=Didact+Gothic&display=swap">
<style>
  :root {
    --stage: #e9e6e1;
    --backdrop-top: #b99a62;
    --backdrop-bottom: #6d7a44;
    --tile-fill: rgba(58, 40, 22, 0.55);
    --tile-edge: rgba(255, 255, 255, 0.18);
    --tile-text: #ffffff;
    --video-frame: rgba(255, 255, 255, 0.12);
    --video-screen: #fcf7f7;
    --play-disc: #d4d4d4;
    --play-arrow: #ffffff;
    --control-blue: #3aaee2;
    --brand-panel: #161a1c;
    --brand-text: #ffffff;
    --brand-accent: #3aaee2;
  }
  * { box-sizing: border-box; margin: 0; padding: 0; }
  html, body {
    width: 1200px;
    height: 758px;
    overflow: hidden;
    background: var(--stage);
    font-family: "Didact Gothic", "Segoe UI", sans-serif;
  }
  .homescreen {
    position: absolute;
    left: 5px;
    top: 38px;
    width: 1190px;
    height: 670px;
    overflow: hidden;
  }
  .backdrop {
    position: absolute;
    inset: 0;
    background: linear-gradient(180deg, var(--backdrop-top), var(--backdrop-bottom));
  }
  .channel-grid {
    position: absolute;
    left: 17px;
    top: 97px;
    display: grid;
    grid-template-columns: repeat(3, 170px);
    grid-template-rows: repeat(3, 135px);
    column-gap: 37px;
    row-gap: 37px;
  }
  .channel-tile {
    display: flex;
    align-items: center;
    justify-content: center;
    background: var(--tile-fill);
    border: 1px solid var(--tile-edge);
    border-radius: 12px;
    box-shadow: 0 2px 6px rgba(0, 0, 0, 0.35);
    color: var(--tile-text);
    font-size: 37px;
    white-space: nowrap;
    text-shadow: 0 1px 2px rgba(0, 0, 0, 0.4);
  }
  .video-panel {
    position: absolute;
    left: 663px;
    top: 175px;
    width: 501px;
    height: 332px;
    border: 1px solid rgba(255, 255, 255, 0.85);
    border-radius: 6px;
    background: var(--video-frame);
    box-shadow: 0 0 6px rgba(0, 0, 0, 0.3);
  }
  .video-screen {
    position: absolute;
    left: 6px;
    top: 6px;
    width: 489px;
    height: 286px;
    background: var(--video-screen);
    border-radius: 4px;
  }
  .play-button {
    position: absolute;
    left: 150px;
    top: 48px;
  }
  .video-controls {
    position: absolute;
    left: 214px;
    top: 296px;
    display: flex;
    gap: 12px;
  }
  .brand-panel {
    position: absolute;
    left: 873px;
    top: 584px;
    width: 317px;
    height: 86px;
    background: var(--brand-panel);
    border-top-left-radius: 60px 86px;
    opacity: 0.92;
  }
  .brand-name {
    position: absolute;
    right: 14px;
    top: 26px;
    display: flex;
    align-items: center;
    gap: 10px;
    color: var(--brand-text);
    font-size: 26px;
    white-space: nowrap;
  }
  .brand-mark {
    width: 12px;
    height: 12px;
    background: var(--brand-accent);
  }
  .brand-tagline {
    position: absolute;
    right: 14px;
    top: 60px;
    color: var(--brand-text);
    font-size: 12px;
    white-space: nowrap;
  }
</style>
</head>
<body>
  <main class="homescreen">
    <div class="backdrop" role="img" aria-label="Landscape photograph placeholder: sunset over a flower meadow"></div>

    <nav class="channel-grid">
      <div class="channel-tile">Cable TV</div>
      <div class="channel-tile">Cable TV</div>
      <div class="channel-tile">Cable TV</div>
      <div class="channel-tile">Cable TV</div>
      <div class="channel-tile">Cable TV</div>
      <div class="channel-tile">Cable TV</div>
      <div class="channel-tile">Cable TV</div>
      <div class="channel-tile">Cable TV</div>
      <div class="channel-tile">Cable TV</div>
    </nav>

    <section class="video-panel" aria-label="Video player">
      <div class="video-screen">
        <svg class="play-button" width="190" height="190" viewBox="0 0 190 190" aria-hidden="true">
          <circle cx="95" cy="95" r="95" fill="var(--play-disc)"/>
          <polygon points="64,42 64,150 160,96" fill="var(--play-arrow)"/>
        </svg>
      </div>
      <div class="video-controls">
        <svg width="24" height="26" viewBox="0 0 24 26" aria-label="Pause">
          <rect x="3" y="3" width="7" height="20" fill="var(--control-blue)"/>
          <rect x="14" y="3" width="7" height="20" fill="var(--control-blue)"/>
        </svg>
        <svg width="34" height="26" viewBox="0 0 34 26" aria-label="Volume">
          <polygon points="2,9 9,9 18,2 18,24 9,17 2,17" fill="var(--control-blue)"/>
          <path d="M23 7 Q28 13 23 19" stroke="var(--control-blue)" stroke-width="2.5" fill="none"/>
        </svg>
      </div>
    </section>

    <footer class="brand-panel">
      <div class="brand-name"><span class="brand-mark"></span>Wellward Systems</div>
      <div class="brand-tagline">improving patient care</div>
    </footer>
  </main>
</body>
</html>
```